Alcohol free flavoured Malt Drink Label design

we are beverage company producer our main brand is Brightwave, we are willing to produce Alcohol free flavoured Malt Drink, this product target new generation should be fresh colourful and modern, the name of the Malt drink is Zeal. so main brand is Brightwave and product name is NUR. the label size: 198mm X 66mm

Dear All
i changed the product name to NUR (means Crown ) this will add more ideas in the design . Thanks

```html
<!DOCTYPE html>
<html lang="en">
<head>
<meta charset="utf-8">
<title>Brightwave NUR – Flavoured Malt Drink Labels</title>
<link rel="stylesheet" href="https://fonts.googleapis.com/css2?family=Oswald:wght@500;600;700&family=Poppins:wght@500;700&display=swap">
<style>
  :root{
    --backdrop:#8e8e8e;
    --label:#f7f7f7;
    --ink:#111111;
    --grape:#6b2a6e;
    --berry:#ee2346;
    --mango:#f37a1f;
    --mango-light:#f5c02c;
    --mango-deep:#e8461c;
    --berry-light:#f0505f;
    --berry-deep:#c81f33;
  }
  *{box-sizing:border-box;margin:0;padding:0}
  html,body{width:1200px;height:815px;overflow:hidden}
  body{background:var(--backdrop);position:relative;font-family:"Oswald",sans-serif}

  .label{
    position:absolute;background:var(--label);
    overflow:hidden;border-radius:6px;
    box-shadow:0 6px 18px rgba(0,0,0,.25);
  }
  .label--blackcurrant{left:70px;top:175px;width:330px;height:545px;--flavour:var(--grape)}
  .label--strawberry{left:430px;top:145px;width:350px;height:590px;--flavour:var(--berry)}
  .label--mango{left:810px;top:175px;width:330px;height:545px;--flavour:var(--mango)}

  .brand{
    position:absolute;top:52px;left:0;right:0;
    font-family:"Poppins",sans-serif;font-weight:700;font-size:34px;
    color:var(--ink);letter-spacing:-0.5px;white-space:nowrap;
    display:flex;align-items:center;justify-content:center;gap:10px;
  }
  .brand__dot{width:16px;height:16px;border-radius:50%;background:var(--ink)}

  .product-name{
    position:absolute;top:112px;left:0;right:0;text-align:center;
    font-family:"Oswald",sans-serif;font-weight:700;font-size:168px;line-height:1;
    color:var(--flavour);letter-spacing:4px;white-space:nowrap;
  }
  .bubble{position:absolute;border-radius:50%;background:var(--label);border:3px solid var(--flavour)}

  .descriptor{
    position:absolute;top:340px;left:0;right:0;
    display:flex;align-items:center;justify-content:center;gap:8px;
    font-family:"Oswald",sans-serif;font-weight:600;font-size:22px;color:var(--ink);
    white-space:nowrap;
  }
  .descriptor__rule{flex:none;width:32px;height:9px;border-top:1.5px solid var(--ink);border-bottom:1.5px solid var(--ink);position:relative}
  .descriptor__rule::after{content:"";position:absolute;left:0;right:0;top:2.5px;border-top:1.5px solid var(--ink)}

  .alcohol-band{
    position:absolute;top:418px;left:30px;width:190px;height:30px;
    background:var(--ink);transform:skewX(-8deg);
    color:#fff;font-family:"Oswald",sans-serif;font-weight:500;font-size:20px;white-space:nowrap;
    display:flex;align-items:center;justify-content:center;
  }
  .alcohol-band span{transform:skewX(8deg)}

  .flavour-box{
    position:absolute;top:450px;left:18px;width:300px;height:56px;
    border:1.5px solid var(--ink);transform:skewX(-6deg);
    display:flex;align-items:center;padding-left:30px;
  }
  .flavour-box span{
    transform:skewX(6deg);white-space:nowrap;
    font-family:"Oswald",sans-serif;font-weight:600;font-size:36px;color:var(--flavour);letter-spacing:.5px;
  }

  .volume{
    position:absolute;bottom:16px;left:0;right:0;text-align:center;white-space:nowrap;
    font-family:"Poppins",sans-serif;font-weight:500;font-size:11px;letter-spacing:2px;color:var(--ink);
  }

  .fruit{position:absolute;border-radius:48%}
  .fruit--strawberry{right:8px;top:412px;width:100px;height:110px;
    background:radial-gradient(circle at 40% 40%,var(--berry-light),var(--berry-deep))}
  .fruit--mango{right:16px;top:378px;width:100px;height:120px;border-radius:55% 45% 50% 50%;
    background:linear-gradient(200deg,var(--mango) 10%,var(--mango-deep) 60%,var(--mango-light) 95%)}
</style>
</head>
<body>

<section class="label label--blackcurrant" aria-label="Blackcurrant label">
  <div class="brand"><span class="brand__dot"></span>Brightwave</div>
  <div class="product-name">NUR</div>
  <span class="bubble" style="left:58px;top:112px;width:26px;height:26px"></span>
  <span class="bubble" style="left:150px;top:252px;width:24px;height:24px"></span>
  <span class="bubble" style="left:250px;top:128px;width:22px;height:22px"></span>
  <div class="descriptor"><span class="descriptor__rule"></span>FLAVOURED MALT DRINK<span class="descriptor__rule"></span></div>
  <div class="alcohol-band"><span>ALCOHOL FREE</span></div>
  <div class="flavour-box"><span>BLACKCURRANT</span></div>
  <div class="volume">0% ALCOHOL | 5OZ | 250ML</div>
</section>

<section class="label label--strawberry" aria-label="Strawberry label">
  <div class="brand"><span class="brand__dot"></span>Brightwave</div>
  <div class="product-name">NUR</div>
  <span class="bubble" style="left:170px;top:110px;width:28px;height:28px"></span>
  <span class="bubble" style="left:66px;top:262px;width:26px;height:26px"></span>
  <span class="bubble" style="left:290px;top:284px;width:22px;height:22px"></span>
  <div class="descriptor"><span class="descriptor__rule"></span>FLAVOURED MALT DRINK<span class="descriptor__rule"></span></div>
  <div class="alcohol-band" style="top:420px"><span>ALCOHOL FREE</span></div>
  <div class="flavour-box" style="top:455px;left:14px;width:222px;padding-left:20px"><span>STRAWBERRY</span></div>
  <div class="fruit fruit--strawberry" role="img" aria-label="Illustration of a whole and a halved strawberry with green leaves"></div>
  <div class="volume">0% ALCOHOL | 5OZ | 250ML</div>
</section>

<section class="label label--mango" aria-label="Mango label">
  <div class="brand"><span class="brand__dot"></span>Brightwave</div>
  <div class="product-name">NUR</div>
  <span class="bubble" style="left:130px;top:114px;width:26px;height:26px"></span>
  <span class="bubble" style="left:258px;top:262px;width:26px;height:26px"></span>
  <span class="bubble" style="left:44px;top:250px;width:20px;height:20px"></span>
  <div class="descriptor"><span class="descriptor__rule"></span>FLAVOURED MALT DRINK<span class="descriptor__rule"></span></div>
  <div class="alcohol-band" style="width:170px"><span>ALCOHOL FREE</span></div>
  <div class="flavour-box" style="width:170px"><span>MANGO</span></div>
  <div class="fruit fruit--mango" role="img" aria-label="Illustration of a ripe mango with a small stem"></div>
  <div class="volume">0% ALCOHOL | 5OZ | 250ML</div>
</section>

</body>
</html>
```